Silverleaf upkeep services strata flyer

Looking for a flyer that will grab peoples attention also need to include some kind off promotional offer on there so they will hold onto the flyer . Would like approximateley 4 pictures of appartment blocks. Would like to include the following services. Building management Common area cleaning ,window cleaning, lawn mowing, gardening , pressure cleaning, carpet cleaning, bin cleaning. Handy man services.

Target Market(s)

appartment blocks/strata managers

Industry/Entity Type

Pressure Cleaning

Font styles to use
Serif

Colors
0355a3
ceddec
ec2027

Requirements
Must have
• company logo & colors contact details email: Info@silverleafupkeepservices.com.au
• Phone: 0438507721 website silverleafupkeepservices.com.au

```html
<!DOCTYPE html>
<html lang="en">
<head>
<meta charset="utf-8">
<title>Silverleaf upkeep services – strata flyer</title>
<link rel="stylesheet" href="https://fonts.googleapis.com/css2?family=PT+Sans:wght@400;700&display=swap">
<style>
  :root {
    --brand-blue: #0355a3;
    --deep-blue: #0a3f86;
    --mid-blue: #3b78c4;
    --pale-blue: #ceddec;
    --offer-red: #ec2027;
    --ink: #1d1d1d;
    --paper: #ffffff;
    --backdrop: #eef1f4;
  }
  * { box-sizing: border-box; margin: 0; padding: 0; }
  html, body {
    width: 1200px; height: 873px; overflow: hidden;
    background: var(--backdrop);
    font-family: "PT Sans", Arial, sans-serif;
  }
  .flyer {
    position: absolute; left: 404px; top: 20px;
    width: 392px; height: 833px;
    background: var(--paper);
    overflow: hidden;
    box-shadow: 0 4px 18px rgba(0,0,0,.18);
  }
  .brand {
    position: absolute; left: 18px; top: 22px;
    display: flex; align-items: center; gap: 10px; z-index: 3;
  }
  .brand-dot {
    width: 46px; height: 46px; border-radius: 50%;
    background: var(--brand-blue);
  }
  .brand-name {
    color: var(--brand-blue); font-weight: 700; font-size: 17px;
    line-height: 1.1; width: 130px;
  }
  .quote-ribbon {
    position: absolute; right: 0; top: 14px; z-index: 3;
    background: var(--offer-red); color: var(--paper);
    font-weight: 700; font-size: 13px; letter-spacing: .3px;
    padding: 5px 16px 5px 22px;
    clip-path: polygon(0 0, 100% 0, 100% 100%, 0 100%, 8px 50%);
  }
  .photo { position: absolute; }
  .photo-tower { left: 0; top: 120px; width: 196px; height: 150px;
    background: linear-gradient(160deg, #c9d3dc, #8a98a6 70%, #5d6b78); }
  .photo-window { left: 198px; top: 96px; width: 194px; height: 174px;
    background: linear-gradient(150deg, #5e7f9a, #9fb7c8 50%, #3e5e86); }
  .photo-low { left: 0; top: 272px; width: 102px; height: 62px;
    background: linear-gradient(180deg, #b9c9d6, #a18878 60%, #6f8a55); }
  .photo-trees { left: 104px; top: 272px; width: 96px; height: 62px;
    background: linear-gradient(180deg, #c7d8e6, #7f9a62 65%, #55703f); }
  .photo-highrise { left: 202px; top: 272px; width: 190px; height: 62px;
    background: linear-gradient(180deg, #7fb3e0, #c7cfd6 55%, #7b8f6a); }
  .wave { position: absolute; left: 0; width: 392px; display: block; }
  .wave-top { top: 70px; height: 90px; z-index: 2; }
  .wave-low { top: 500px; height: 90px; z-index: 2; }
  .services-title {
    position: absolute; left: 28px; top: 346px;
    color: var(--brand-blue); font-weight: 700; font-size: 23px;
    line-height: .98; text-transform: uppercase;
  }
  .service-list {
    position: absolute; top: 404px; list-style: none;
    font-size: 15.5px; color: var(--ink); line-height: 21px;
  }
  .service-list.col-a { left: 26px; }
  .service-list.col-b { left: 226px; top: 394px; }
  .service-list li { display: flex; align-items: center; gap: 8px; white-space: nowrap; }
  .service-list li::before {
    content: "›"; display: inline-flex; align-items: center; justify-content: center;
    width: 11px; height: 11px; border-radius: 50%;
    background: var(--offer-red); color: var(--paper);
    font-size: 11px; font-weight: 700; line-height: 1; padding-bottom: 1px;
  }
  .contact-panel {
    position: absolute; left: 0; top: 560px; width: 392px; height: 210px;
    background: var(--pale-blue);
  }
  .offer-line {
    position: absolute; top: 594px; width: 100%; text-align: center;
    color: var(--offer-red); font-size: 14.5px; z-index: 3;
  }
  .offer-terms {
    position: absolute; top: 612px; width: 100%; text-align: center;
    color: var(--ink); font-size: 11px; z-index: 3;
  }
  .phone-box {
    position: absolute; left: 50px; top: 634px; width: 292px; height: 60px;
    border: 1.5px dotted #a9b7c6; background: #e4ecf4;
    display: flex; align-items: center; justify-content: center; gap: 14px;
  }
  .phone-number { color: var(--offer-red); font-weight: 700; font-size: 30px; letter-spacing: .5px; }
  .email {
    position: absolute; top: 710px; width: 100%; text-align: center;
    color: var(--brand-blue); font-size: 17px;
  }
  .web-band {
    position: absolute; left: 0; bottom: 0; width: 392px; height: 70px;
    background: var(--brand-blue);
    border-top: 6px solid var(--mid-blue);
    display: flex; align-items: center; justify-content: center;
    color: var(--paper); font-size: 20px;
  }
</style>
</head>
<body>
<article class="flyer">
  <header>
    <div class="brand"><span class="brand-dot"></span><span class="brand-name">Silverleaf upkeep services</span></div>
    <div class="quote-ribbon">FREE QUOTES!</div>
  </header>

  <div class="photo photo-tower" role="img" aria-label="Modern apartment tower with balconies"></div>
  <div class="photo photo-window" role="img" aria-label="Window cleaner washing apartment glass with an extension pole"></div>
  <div class="photo photo-low" role="img" aria-label="Low-rise brick apartment block"></div>
  <div class="photo photo-trees" role="img" aria-label="Apartment building behind garden trees"></div>
  <div class="photo photo-highrise" role="img" aria-label="High-rise apartment blocks under blue sky"></div>

  <svg class="wave wave-top" viewBox="0 0 392 90" preserveAspectRatio="none" aria-hidden="true">
    <path d="M0 0 H392 V40 C300 20 220 40 150 62 C90 80 40 70 0 58 Z" fill="#ffffff"/>
    <path d="M0 58 C40 70 90 80 150 62 C220 40 300 20 392 40 V52 C300 30 220 52 150 72 C90 90 40 82 0 70 Z" fill="var(--brand-blue)"/>
    <path d="M0 70 C40 82 90 90 150 72 C220 52 300 30 392 52 V58 C300 38 220 60 150 80 C90 96 40 88 0 78 Z" fill="var(--pale-blue)"/>
  </svg>

  <h2 class="services-title">Our cleaning<br>services include:</h2>
  <ul class="service-list col-a">
    <li>Building Management</li>
    <li>Common Area Cleaning</li>
    <li>Window Cleaning</li>
    <li>Lawn Mowing</li>
    <li>Gardening</li>
  </ul>
  <ul class="service-list col-b">
    <li>Pressure Cleaning</li>
    <li>Carpet Cleaning</li>
    <li>Bin Cleaning</li>
    <li>Handy Man Services</li>
  </ul>

  <div class="contact-panel"></div>
  <svg class="wave wave-low" viewBox="0 0 392 90" preserveAspectRatio="none" aria-hidden="true">
    <path d="M0 62 C90 86 180 78 260 40 C310 18 360 14 392 20 V90 H0 Z" fill="var(--pale-blue)"/>
    <path d="M0 58 C90 82 180 72 260 34 C310 12 360 8 392 14 V26 C360 20 310 26 262 48 C180 86 90 92 0 68 Z" fill="var(--brand-blue)"/>
    <path d="M0 68 C90 92 180 86 262 48 C310 26 360 20 392 26 V32 C360 28 312 34 266 56 C182 94 90 98 0 76 Z" fill="var(--mid-blue)"/>
  </svg>

  <p class="offer-line">Present This Brochure For Your Free Initial Clean</p>
  <p class="offer-terms">conditions apply &amp; offer ends 31/07/2015</p>

  <div class="phone-box">
    <svg width="40" height="34" viewBox="0 0 40 34" aria-hidden="true">
      <path d="M3 10 C3 3 37 3 37 10 V13 H29 V9 H11 V13 H3 Z" fill="var(--offer-red)"/>
      <path d="M12 12 H28 L34 30 H6 Z" fill="var(--offer-red)"/>
      <g fill="#ffffff">
        <circle cx="15" cy="18" r="1.6"/><circle cx="20" cy="18" r="1.6"/><circle cx="25" cy="18" r="1.6"/>
        <circle cx="14" cy="23" r="1.6"/><circle cx="20" cy="23" r="1.6"/><circle cx="26" cy="23" r="1.6"/>
      </g>
    </svg>
    <span class="phone-number">043 850 7721</span>
  </div>
  <p class="email">Info@silverleafupkeepservices.com.au</p>

  <footer class="web-band">www.silverleafupkeepservices.com.au</footer>
</article>
</body>
</html>
```